Business Card Design Project

A double sided business card for presentation to business leaders in corporate.

Target Market(s)

Corporate, business professionals, HR

Industry/Entity Type

Business

Requirements
Must have
• FRONT

Logo

www.brightlanecoaching.com.au

BACK

Mara Pollen-Drew
Director

+ 61 (0) 418 536 204
mara@brightlanecoaching.com.au
www.brightlanecoaching.com.au

Momentum through clarity and confident teamwork

("ripples" of logo, bottom corner)

Must be:
- double sided
size: 86 x 54mm
supplied as one pdf with crop marks shown (+- 1mm, with 2-3 mm bleed)

```html
<!DOCTYPE html>
<html lang="en">
<head>
<meta charset="utf-8">
<title>Bright Lane Coaching – Business Card</title>
<link rel="stylesheet" href="https://fonts.googleapis.com/css2?family=Montserrat:wght@300;400;600&display=swap">
<style>
  :root {
    --paper: #ffffff;
    --ink: #1a1a1a;
    --frame: #111111;
    --brand-purple: #6a0d91;
    --brand-grey: #3f4447;
    --on-purple: #ffffff;
  }
  * { box-sizing: border-box; margin: 0; padding: 0; }
  html, body {
    width: 1200px;
    height: 902px;
    overflow: hidden;
    background: var(--paper);
  }
  body {
    position: relative;
    font-family: "Montserrat", "Century Gothic", sans-serif;
    color: var(--ink);
  }
  .board {
    position: absolute;
    left: 1px; top: 1px;
    width: 1198px; height: 900px;
    border: 2px solid var(--frame);
  }
  .card {
    position: absolute;
    left: 345px;
    width: 512px;
    height: 321px;
  }
  .card--front {
    top: 103px;
    background: var(--paper);
    border: 2px solid var(--frame);
  }
  .card--back {
    top: 480px;
    background: var(--brand-purple);
    color: var(--on-purple);
  }

  /* Front */
  .wordmark {
    position: absolute;
    display: flex;
    align-items: center;
    gap: 12px;
    font-weight: 400;
    white-space: nowrap;
  }
  .card--front .wordmark {
    left: 0; right: 0;
    top: 108px;
    justify-content: center;
    font-size: 32px;
    color: var(--brand-purple);
  }
  .wordmark__dot {
    width: 14px; height: 14px;
    border-radius: 50%;
    background: currentColor;
    flex: none;
  }
  .front-url {
    position: absolute;
    left: 0; right: 0;
    top: 238px;
    text-align: center;
    font-size: 16px;
    font-weight: 400;
    color: var(--ink);
  }

  /* Back */
  .holder {
    position: absolute;
    left: 51px;
    top: 67px;
    white-space: nowrap;
  }
  .holder__name {
    font-size: 19px;
    font-weight: 600;
    letter-spacing: 2px;
  }
  .holder__role {
    font-size: 14px;
    font-weight: 300;
    letter-spacing: 1.6px;
    margin-left: 3px;
  }
  .contact {
    position: absolute;
    left: 234px;
    top: 117px;
    list-style: none;
    font-size: 14.5px;
    font-weight: 300;
    line-height: 27.5px;
    white-space: nowrap;
  }
  .tagline {
    position: absolute;
    left: 234px;
    top: 224px;
    font-size: 16px;
    font-weight: 300;
    line-height: 20px;
    white-space: nowrap;
  }
  .card--back .wordmark {
    left: 51px;
    top: 216px;
    gap: 8px;
    font-size: 16px;
    line-height: 19px;
    color: var(--on-purple);
  }
  .card--back .wordmark__dot {
    width: 10px; height: 10px;
  }
</style>
</head>
<body>
  <div class="board"></div>

  <section class="card card--front" aria-label="Card front">
    <div class="wordmark">
      <span class="wordmark__dot"></span>
      <span class="wordmark__name">Bright Lane Coaching</span>
    </div>
    <p class="front-url">www.brightlanecoaching.com.au</p>
  </section>

  <section class="card card--back" aria-label="Card back">
    <p class="holder">
      <span class="holder__name">Mara Pollen-Drew</span>
      <span class="holder__role">director</span>
    </p>
    <ul class="contact">
      <li>+ 61 (0) 418 536 204</li>
      <li>mara@brightlanecoaching.com.au</li>
      <li>www.brightlanecoaching.com.au</li>
    </ul>
    <p class="tagline">Momentum through clarity and<br>confident teamwork</p>
    <div class="wordmark">
      <span class="wordmark__dot"></span>
      <span class="wordmark__name">Bright Lane<br>Coaching</span>
    </div>
  </section>
</body>
</html>
```